Soccer Club Site Redesign

We are a suburban youth soccer club in need of a web site redesign. Our current site’s look/feel is outdated and is in need of a more modern look. What we are looking for is a design layout that will accommodate the current functionality we have for the site and give us an updated modern look. The deliverable for this project will be .psd file that can be converted to an html theme file for Wordpress. We will take care of the conversion and handle the html coding/javascript functionality.
Take a look at our current site to get an idea of what we offer and the current layout we have.
http://www.torvelkicks.org
Our club hosts youth recreational soccer, traveling soccer and two large soccer tournaments during the year. We also sponsor a number of training clinics. Our site serves a couple primary purposes:
1. Parents learn how/where/when to sign up their child for the leagues we offer.
2. Parents learn dates/times of various events the club offers.
3. Other soccer clubs get information on the tournaments we offer, sign up for the tournaments etc.
We do a pretty good job of presenting information about the various events/leagues available and how to sign up for them, but we want to do a better job of presenting a calendar where parents can quickly find dates/times of various events. Ideally, we would like to incorporate a news section (like we currently have), with a calendar and the use of more images on the home page. We understand screen space is limited but would incorporate jquery/javascript widgets to hide/show info and maybe an ‘imagebox’ for the additional images.
Here are a few sites with ideas that we liked:
http://sports.brenwickcollege.edu/ (Look at the Upcoming Events calendar on the page)
http://www.fennlowfutbol.com/ (look at the Upcoming Events calendar in the right column and the image box in the main content area)
http://www.rundlekick.com/index.php (Like the look and use of images)
http://www.qvfootyclub.com/ (imagebox use)
http://www.sarvapuckclub.org/ ( hockey website but like the use of crisp header graphics)
http://www.delvingpuckers.com/ (another hockey site, like the calendar used)
That should give you a pretty good idea of what we are looking for. The new design will need to accommodate the existing functionality of the site. Our logo (which is attached) should be incorporated into the site….otherwise we are open to your design ideas.

```html
<!DOCTYPE html>
<html lang="en">
<head>
<meta charset="utf-8">
<title>Torvel Soccer Club</title>
<link rel="stylesheet" href="https://fonts.googleapis.com/css2?family=PT+Sans:wght@400;700&family=Signika:wght@400;600&family=Open+Sans+Condensed:wght@700&display=swap">
<style>
:root{
  --navy:#23288a;
  --royal:#2b3aa6;
  --sky:#2f7fe0;
  --black:#000;
  --panel-top:#f4f4f6;
  --panel-bot:#b9b9bf;
  --panel-edge:#c9c9f0;
  --gold:#e8c23a;
  --gold-dark:#b8860b;
  --red:#a5000b;
  --green:#3fa534;
  --white:#fff;
  --ink:#111;
  --warm:#d89a2a;
}
*{margin:0;padding:0;box-sizing:border-box}
html,body{width:1200px;height:748px;overflow:hidden;background:var(--black)}
.page{position:relative;width:1200px;height:748px;overflow:hidden;font-family:"PT Sans",sans-serif;color:var(--ink)}
.header{position:absolute;left:0;top:0;width:1200px;height:100px;background:linear-gradient(180deg,#dfe9f5 0%,#f7f9fc 55%,#fff 100%)}
.club-mark{position:absolute;left:188px;top:32px;display:flex;align-items:center;gap:8px;font-weight:700;font-size:22px;color:var(--navy)}
.club-mark .dot{width:34px;height:34px;border-radius:50%;background:var(--navy)}
.site-title{position:absolute;left:356px;top:0;font-family:"Signika",sans-serif;font-weight:600;font-size:80px;letter-spacing:-1px;color:var(--sky);line-height:100px}
.nav{position:absolute;left:0;top:100px;width:1200px;height:30px;background:var(--black);display:flex;justify-content:center;gap:15px;align-items:center}
.nav a{font-family:"Open Sans Condensed",sans-serif;font-weight:700;font-size:12px;color:var(--white);text-decoration:none;text-transform:uppercase}
.stage{position:absolute;left:0;top:130px;width:1200px;height:462px;background:linear-gradient(90deg,#050510 0%,#1e2a8f 20%,#2a3aae 50%,#1e2a8f 80%,#050510 100%);border-top:2px solid #4a55c8;border-bottom:1px solid #4a55c8}
.side-art{position:absolute;top:0;width:160px;height:459px}
.side-art.left{left:0;background:linear-gradient(90deg,#141428 0%,var(--warm) 65%,rgba(30,42,143,0) 100%)}
.side-art.right{right:0;background:linear-gradient(270deg,#141428 0%,var(--warm) 65%,rgba(30,42,143,0) 100%)}
.panel{position:absolute;border:3px solid var(--panel-edge);border-radius:6px;background:linear-gradient(180deg,var(--panel-top),var(--panel-bot))}
.panel-tab{position:absolute;left:10px;right:10px;top:-3px;height:40px;background:linear-gradient(180deg,#5560d8,var(--navy));border-radius:0 0 60% 60%/0 0 14px 14px;color:var(--white);font-family:"Signika",sans-serif;font-weight:600;font-style:italic;font-size:18px;text-align:center;line-height:36px}
.events{left:170px;top:4px;width:193px;height:247px}
.event{position:absolute;left:12px;width:168px;display:flex;gap:8px;font-size:12px;line-height:13px}
.event .date{width:40px;height:46px;background:linear-gradient(180deg,#2a8fe4,#0a56b8);clip-path:polygon(0 0,100% 0,100% 80%,50% 100%,0 80%);color:var(--white);font-size:11px;text-align:center;padding-top:8px;line-height:13px}
.event .rule{position:absolute;left:70px;right:8px;bottom:-8px;border-bottom:1px dotted #777}
.learn{position:absolute;right:10px;font-size:9px;font-weight:700;color:var(--red);display:flex;align-items:center;gap:4px}
.learn i{width:11px;height:11px;border-radius:50%;background:#ddd;border:1px solid #999}
.photo{position:absolute;left:374px;top:5px;width:656px;height:246px;border-radius:6px;background:linear-gradient(180deg,#cfd6cf 0%,#5f6e8a 35%,#1f2860 75%,#5c8f3a 100%)}
.news{left:170px;top:264px;width:193px;height:189px}
.news ul{position:absolute;top:50px;left:8px;list-style:none;font-size:11px;line-height:16.7px}
.news li::before{content:"";display:inline-block;width:0;height:0;border-left:7px solid var(--green);border-top:4px solid transparent;border-bottom:4px solid transparent;margin-right:5px}
.welcome{left:374px;top:264px;width:656px;height:189px}
.welcome h1{position:absolute;left:14px;top:2px;font-family:"Signika",sans-serif;font-weight:400;font-size:25px;color:var(--navy)}
.welcome p{position:absolute;left:12px;top:33px;width:628px;font-size:11.5px;line-height:13px}
.reg{position:absolute;top:95px;width:202px;height:82px;border-radius:5px;background:linear-gradient(180deg,#4a58d0,var(--navy));box-shadow:0 3px 4px rgba(0,0,0,.4)}
.reg .yr{position:absolute;left:12px;top:8px;font-family:"Signika",sans-serif;font-size:24px;color:var(--white)}
.reg .what{position:absolute;left:83px;top:12px;font-size:12.5px;line-height:13px;color:var(--gold)}
.reg .btn{position:absolute;left:46px;top:52px;width:122px;height:22px;border-radius:2px;background:linear-gradient(180deg,#f6d860,var(--gold-dark));border:1px solid #8a6a00;text-align:center;font-size:14px;font-weight:700;line-height:20px;color:#2a1a00}
.foot-nav{position:absolute;left:0;top:600px;width:1200px;display:flex;justify-content:center;gap:13px;font-size:10px;color:var(--white)}
.glow{position:absolute;left:100px;top:632px;width:1000px;height:8px;background:radial-gradient(ellipse at center,#2ab0e8 0%,rgba(0,0,0,0) 70%)}
.partners{position:absolute;left:500px;top:661px;width:203px;height:77px;background:var(--white);display:flex;align-items:center;justify-content:space-around}
.partners span{width:80px;height:54px;background:#c8c8d0}
.social{position:absolute;left:912px;top:686px;display:flex;gap:14px;font-size:13px;font-weight:700;color:var(--white)}
.social span{display:flex;align-items:center;gap:5px}
.social b{width:12px;height:12px;background:#3a7ad0}
.copy{position:absolute;left:183px;top:723px;font-size:10px;color:var(--white)}
</style>
</head>
<body>
<div class="page">
  <header class="header">
    <div class="club-mark"><span class="dot"></span>Torvel</div>
    <div class="site-title">Torvel Soccer Club</div>
  </header>
  <nav class="nav">
    <a>Home</a><a>About Us</a><a>Forms</a><a>Calendar</a><a>Traveling</a><a>Recreational</a><a>Tournaments</a><a>Referees</a><a>Field Maps</a><a>Coaches</a><a>Team Manager</a><a>Blog</a><a>Contact Us</a>
  </nav>
  <main class="stage">
    <div class="side-art left" role="img" aria-label="Decorative side artwork"></div>
    <div class="side-art right" role="img" aria-label="Decorative side artwork"></div>

    <section class="panel events">
      <div class="panel-tab">Upcoming Events</div>
      <div class="event" style="top:50px"><div class="date">Dec 10<br>2012</div><div>17.00<br>Travel Soccer<br>Torvel High School</div><span class="rule"></span></div>
      <div class="event" style="top:114px"><div class="date">Dec 10<br>2012</div><div>17.00<br>Travel Soccer<br>Torvel High School</div><span class="rule"></span></div>
      <div class="event" style="top:176px"><div class="date">Dec 10<br>2012</div><div>17.00<br>Travel Soccer<br>Torvel High School</div></div>
      <div class="learn" style="bottom:4px">Learn more <i></i></div>
    </section>

    <div class="photo" role="img" aria-label="Youth soccer team in navy jerseys posing on a grass field"></div>

    <section class="panel news">
      <div class="panel-tab">News</div>
      <ul>
        <li>Torvel High School Boys and ..</li>
        <li>NYSA Fall State Champion..</li>
        <li>Summer Travel 2013 - Roster..</li>
        <li>Dana Merrow Memorial Youth ..</li>
        <li>2013 Summer Travel ..</li>
        <li>NYSA State Champions..</li>
        <li>PSL Launches New Kids' ..</li>
      </ul>
      <div class="learn" style="bottom:4px">Learn more <i></i></div>
    </section>

    <section class="panel welcome">
      <h1>Welcome to the Torvel Soccer Club!</h1>
      <p>Torvel Soccer Club is a community based recreational and traveling soccer programs that are open to all residents of Independent School District #16 and #11 as well as other surrounding communities. Torvel Soccer Club is affiliated with the City of Torvel Park and Recreation Department and the Northlake Youth Soccer Association (NYSA).</p>
      <div class="learn" style="top:78px">Learn more <i></i></div>
      <div class="reg" style="left:12px"><span class="yr">2013</span><span class="what">Travel Soccer</span><span class="btn">Register Here</span></div>
      <div class="reg" style="left:225px"><span class="yr">2013</span><span class="what">Travel Soccer<br>Waiting List</span><span class="btn">Register Here</span></div>
      <div class="reg" style="left:439px"><span class="yr">2013</span><span class="what">Fall Recreational<br>Soccer League</span><span class="btn">Register Here</span></div>
    </section>
  </main>

  <footer>
    <div class="foot-nav"><span>Home</span><span>About us</span><span>Forms</span><span>Calendar</span><span>Traveling</span><span>Recreational</span><span>Tournaments</span><span>Referees</span><span>Field Maps</span><span>Coaches</span><span>Team Manager</span><span>Blog</span><span>Volunteers</span><span>Sponsors</span><span>Links</span><span>Contact us</span></div>
    <div class="glow"></div>
    <div class="partners"><span></span><span></span></div>
    <div class="social"><span><b></b>Friendly</span><span><b></b>Chirpa</span></div>
    <div class="copy">Copyright 2012 Torvel Soccer Club 2011. All rights reserved.</div>
  </footer>
</div>
</body>
</html>
```